Non fiction book cover. The book advises how to get a new job.

The book size will be 20cm high by 13cm wide and I need a front cover which can wrap around to the back. This book has a serious message, but I've tried to make it quite light to read and accessible. So I don't want a cover that is too dour or serious and not frivolous either. At the end of the project, I will need a high resolution 3D image of the book, included as part of the package.<br/>The Title of the book is:- "Past Fifty? Hunting for your new role?<br/>by Colin Marsh-Whitby".<br/>I am thinking of a light yellow background, with a striking image to attract attention. The image and words should be clear and sharp.<br/>Here is the, BACK COVER wording.<br/>"This book tells you clearly and simply the steps that you need to take, to get a job, once you’re over 50.<br/>It advises you on the techniques to use to write a killer CV.<br/>It explains how to ensure that your CV attention.<br/>It shows the best way to approach your local job agency.<br/>It demonstrates the best way to use your network.<br/><br/>This book, written by someone with 30 years’ experience in the recruitment industry, gives you ALL the answers.<br/>Whether you are a top executive or someone after some local part time work, then this book is for you. <br/>With the help of this book you will secure your next position.<br/>

Target Market(s)

UK, over 50s, male and female.

Font styles to use
Serif

Colors
fbee3e

Requirements
Must have
• A clear uncluttered cover.
Should not have
• Fussy and over complicated

```html
<!DOCTYPE html>
<html lang="en">
<head>
<meta charset="utf-8">
<title>Past Fifty? Hunting for your new role? — Cover Wrap</title>
<link rel="stylesheet" href="https://fonts.googleapis.com/css2?family=Bebas+Neue&family=Cinzel:wght@700&family=Cormorant+Garamond:wght@400&family=Crimson+Text:wght@400&display=swap">
<style>
  :root {
    --page-bg: #e9e6dc;
    --cover-yellow: #fbee3e;
    --title-red: #d42a3c;
    --accent-teal: #1aa79a;
    --ink: #2b2a26;
    --blush: #e0707a;
    --box-white: #ffffff;
  }
  * { margin: 0; padding: 0; box-sizing: border-box; }
  html, body { width: 1200px; height: 800px; overflow: hidden; }
  body { background: var(--page-bg); position: relative; }

  .wrap {
    position: absolute; left: 85px; top: 21px;
    width: 1030px; height: 758px;
    background: var(--cover-yellow);
    display: flex;
    box-shadow: 0 4px 14px rgba(0,0,0,.18);
  }

  /* Back cover */
  .back { width: 483px; height: 100%; position: relative; padding: 44px 42px 0 46px; }
  .back-kicker {
    text-align: center; color: var(--accent-teal);
    font: 400 30px/1 "Cormorant Garamond", serif;
  }
  .back-title {
    text-align: center; color: var(--title-red);
    font: 400 40px/1 "Bebas Neue", sans-serif; margin-top: 2px; letter-spacing: .3px;
  }
  .blurb { font: 400 13.4px/1.4 "Crimson Text", serif; color: var(--ink); text-align: justify; }
  .blurb-intro { margin-top: 18px; }
  .tick-list { list-style: none; margin: 16px 0 0 16px; }
  .tick-list li { display: flex; gap: 14px; margin-bottom: 16px; }
  .tick-list svg { flex: 0 0 26px; width: 26px; height: 22px; margin-top: 2px; }
  .blurb-outro { margin-top: 14px; }
  .back-art {
    position: absolute; left: 52px; bottom: 0; width: 200px; height: 170px;
    background: linear-gradient(160deg, var(--cover-yellow) 30%, var(--blush) 65%, var(--accent-teal));
  }
  .isbn-box { position: absolute; right: 50px; bottom: 34px; width: 128px; height: 68px; background: var(--box-white); }

  /* Spine */
  .spine {
    width: 58px; height: 100%;
    display: flex; flex-direction: column; align-items: center;
    padding-top: 46px;
  }
  .spine-title, .spine-author { writing-mode: vertical-rl; white-space: nowrap; }
  .spine-title { display: flex; align-items: center; gap: 8px; }
  .spine-title .kicker { font: 400 22px/1 "Cormorant Garamond", serif; color: var(--accent-teal); }
  .spine-title .main { font: 400 28px/1 "Bebas Neue", sans-serif; color: var(--title-red); }
  .spine-author { margin-top: 40px; font: 400 17px/1 "Crimson Text", serif; color: var(--ink); letter-spacing: .5px; }

  /* Front cover */
  .front { width: 489px; height: 100%; position: relative; text-align: center; }
  .front-author {
    margin-top: 40px; color: var(--ink);
    font: 700 26px/1 "Cinzel", serif; letter-spacing: .3px;
  }
  .front-kicker { margin-top: 18px; color: var(--accent-teal); font: 400 66px/1 "Cormorant Garamond", serif; }
  .front-title {
    margin-top: 8px; color: var(--title-red);
    font: 400 92px/.9 "Bebas Neue", sans-serif; letter-spacing: 1px;
  }
  .front-art {
    position: absolute; left: 30px; right: 20px; bottom: 0; height: 330px;
    background: linear-gradient(165deg, var(--cover-yellow) 25%, var(--blush) 60%, var(--accent-teal) 95%);
  }
</style>
</head>
<body>
  <div class="wrap">
    <section class="back">
      <p class="back-kicker">PAST FIFTY?</p>
      <h2 class="back-title">HUNTING FOR YOUR NEW ROLE?</h2>
      <p class="blurb blurb-intro">Lorem ipsum dolor sit amet, consectetur adipisicing elit, sed do eiusmod tempor incididunt ut labore et dolore magna aliqua.</p>
      <ul class="tick-list">
        <li><svg viewBox="0 0 26 22"><rect x="1" y="5" width="16" height="16" fill="none" stroke="#d42a3c" stroke-width="2"/><path d="M5 12l4 5L24 2" fill="none" stroke="#d42a3c" stroke-width="3"/></svg><p class="blurb">Lorem ipsum dolor sit amet, consectetur adipisicing elit, sed do eiusmod tempor incididunt ut labore et dolore magna aliqua.</p></li>
        <li><svg viewBox="0 0 26 22"><rect x="1" y="5" width="16" height="16" fill="none" stroke="#d42a3c" stroke-width="2"/><path d="M5 12l4 5L24 2" fill="none" stroke="#d42a3c" stroke-width="3"/></svg><p class="blurb">Lorem ipsum dolor sit amet, consectetur adipisicing elit, sed do eiusmod tempor incididunt ut labore et dolore magna aliqua.</p></li>
        <li><svg viewBox="0 0 26 22"><rect x="1" y="5" width="16" height="16" fill="none" stroke="#d42a3c" stroke-width="2"/><path d="M5 12l4 5L24 2" fill="none" stroke="#d42a3c" stroke-width="3"/></svg><p class="blurb">Lorem ipsum dolor sit amet, consectetur adipisicing elit, sed do eiusmod tempor incididunt ut labore et dolore magna aliqua.</p></li>
        <li><svg viewBox="0 0 26 22"><rect x="1" y="5" width="16" height="16" fill="none" stroke="#d42a3c" stroke-width="2"/><path d="M5 12l4 5L24 2" fill="none" stroke="#d42a3c" stroke-width="3"/></svg><p class="blurb">Lorem ipsum dolor sit amet, consectetur adipisicing elit, sed do eiusmod tempor incididunt ut labore et dolore magna aliqua.</p></li>
      </ul>
      <p class="blurb blurb-outro">Lorem ipsum dolor sit amet, consectetur adipisicing elit, sed do eiusmod tempor incididunt ut labore et dolore magna aliqua.</p>
      <div class="back-art" role="img" aria-label="Small illustration of a hiker sitting on a faceted teal and pink mountain peak among clouds"></div>
      <div class="isbn-box"></div>
    </section>

    <section class="spine">
      <div class="spine-title"><span class="kicker">PAST FIFTY?</span><span class="main">HUNTING FOR YOUR NEW ROLE?</span></div>
      <div class="spine-author">COLIN MARSH-WHITBY</div>
    </section>

    <section class="front">
      <p class="front-author">COLIN MARSH-WHITBY</p>
      <p class="front-kicker">PAST FIFTY?</p>
      <h1 class="front-title">HUNTING FOR<br>YOUR NEW<br>ROLE?</h1>
      <div class="front-art" role="img" aria-label="Illustration of a hiker with a backpack sitting atop a faceted teal and pink mountain peak, with a thought cloud above and pink and teal clouds around"></div>
    </section>
  </div>
</body>
</html>
```